Norvale Email Signature Banners – Fabrication Capability Series

www.Norvale.com.au is an Australian engineering and fabrication company specialising in fabrication and welding of :
steel piping spools,
skids and frames,
small volume process steel tanks
and general steel fabrication
We require four distinct banner designs for use in Teldrin Quillmark email signatures. Each banner will highlight a specific capability while maintaining a consistent brand identity.
Deliverables
Four banners total:
Piping Spools Fabrication – focus on precision welding and stainless steel pipework
Skid & Frames Fabrication – highlight skid systems and structural frames
Small Steel Tanks Fabrication – show fabricated tanks and workshop craftsmanship
General Fabrication Solutions – broad steel fabrication theme for company-wide use
Dimensions: 600–700 px wide × 100 px high
Format: PNG (preferred), small file size prefered
Resolution: 72 dpi
Background: non-transparent, industrial or workshop setting
Text examples:
1. Piping Spools Fabrication
Option A: “Expert Fabrication Solutions for Process Piping”
Option B: “Precision Welding for Complex Systems”
Option C: “Delivering Quality in Every Spool”
Option D: “Engineered for Flow, Built for Strength”
2. Skid & Frames Fabrication
Option A: “Custom Engineered Modular Systems”
Option B: “Built Strong. Designed Smart.”
Option C: “Reliable Frames for Industrial Performance”
Option D: “Modular Fabrication for Seamless Integration”
3. Small Steel Tanks Fabrication
Option A: “Precision Built for Your Needs”
Option B: “Compact Strength. Proven Durability.”
Option C: “Fabricated for Performance and Longevity”
Option D: “Small Tanks. Big Reliability.”
4. General Fabrication Solutions
Option A: “Quality Craftsmanship, Proven Results”
Option B: “Your Partner in Precision Fabrication”
Option C: “Engineering Excellence in Every Weld”
Option D: “Australian Fabrication. Global Standards.”
Style Direction
Clean, professional, and engineering‑focused
Use Norvale brand colours
Blend photo realism with vector clarity (no heavy gradients)
Include subtle industrial textures or workshop imagery
Typography: bold sans‑serif, legible at small scale
Usage Context
These banners will appear at the bottom of staff email signatures via Quillmark Email Signature Tool for Teldrin 365, so clarity and fast loading are essential. No Logo is required in the banners.
Reference
Existing Norvale signature is attached. Colour palette to match the signature style and logo.
Target Market(s)
Engineering and construction companies,
Industry/Entity Type
Engineering fabrication design

```html
<!DOCTYPE html>
<html lang="en">
<head>
<meta charset="utf-8">
<title>Norvale Email Signature Banner</title>
<link rel="stylesheet" href="https://fonts.googleapis.com/css2?family=Poppins:wght@500;600;700;800&display=swap">
<style>
  :root {
    --brand-blue: #1ea1dd;
    --deep-blue: #1450a8;
    --steel-grey: #878a8e;
    --paper: #ffffff;
    --page: #ffffff;
  }
  html, body {
    margin: 0;
    padding: 0;
    width: 1200px;
    height: 551px;
    overflow: hidden;
    background: var(--page);
    font-family: "Poppins", sans-serif;
  }
  .canvas {
    position: relative;
    width: 1200px;
    height: 551px;
    overflow: hidden;
  }
  .signature {
    position: absolute;
    left: 0;
    top: 76px;
    width: 1200px;
    height: 399px;
    background: var(--paper);
    overflow: hidden;
  }
  .signature-band {
    position: absolute;
    inset: 0;
    width: 1200px;
    height: 399px;
  }
  .brand-name {
    position: absolute;
    left: 0;
    width: 366px;
    top: 83px;
    margin: 0;
    text-align: center;
    font-size: 42px;
    font-weight: 600;
    line-height: 1;
    letter-spacing: 1px;
    color: var(--brand-blue);
  }
  .brand-services {
    position: absolute;
    left: 26px;
    width: 300px;
    top: 300px;
    margin: 0;
    text-align: center;
    font-size: 12px;
    font-weight: 700;
    line-height: 1;
    letter-spacing: 0.3px;
    color: var(--steel-grey);
  }
  .divider {
    position: absolute;
    left: 384px;
    top: 35px;
    width: 3px;
    height: 213px;
    background: var(--brand-blue);
  }
  .person-name {
    position: absolute;
    left: 446px;
    top: 93px;
    margin: 0;
    font-size: 32px;
    font-weight: 500;
    line-height: 1;
    color: var(--brand-blue);
    white-space: nowrap;
  }
  .person-role {
    position: absolute;
    left: 446px;
    top: 134px;
    margin: 0;
    font-size: 21px;
    font-weight: 500;
    line-height: 29px;
    letter-spacing: 0.5px;
    color: var(--steel-grey);
  }
  .contact-list {
    position: absolute;
    left: 0;
    top: 0;
    margin: 0;
    padding: 0;
    list-style: none;
  }
  .contact-item {
    position: absolute;
    left: 763px;
    display: flex;
    align-items: flex-start;
    white-space: nowrap;
    font-size: 21px;
    font-weight: 500;
    line-height: 1;
    color: var(--steel-grey);
  }
  .contact-item .contact-icon {
    width: 26px;
    height: 26px;
    margin-right: 11px;
    flex: none;
    fill: var(--brand-blue);
  }
  .contact-phone { top: 56px; }
  .contact-web { top: 96px; }
  .contact-mail { top: 136px; }
  .contact-address { top: 175px; line-height: 28px; }
  .contact-phone .contact-text,
  .contact-web .contact-text,
  .contact-mail .contact-text { padding-top: 2px; }
  .contact-address .contact-icon { margin-top: 2px; }
  .capability-line {
    position: absolute;
    left: 0;
    width: 1200px;
    top: 349px;
    margin: 0;
    text-align: center;
    font-size: 22px;
    font-weight: 800;
    line-height: 1;
    color: var(--paper);
  }
</style>
</head>
<body>
<main class="canvas">
  <section class="signature">
    <svg class="signature-band" viewBox="0 0 2224 740" preserveAspectRatio="none" aria-hidden="false">
      <defs>
        <radialGradient id="sparkGlow" cx="1110" cy="580" r="620" gradientUnits="userSpaceOnUse">
          <stop offset="0" stop-color="#4a86d4"/>
          <stop offset="0.45" stop-color="#2b67bd"/>
          <stop offset="1" stop-color="#1450a8" stop-opacity="0"/>
        </radialGradient>
        <clipPath id="bandClip">
          <path d="M0,300 L40,320 L100,540 L48,540 L60,608 L602,608 L612,560 L1110,418 L1680,580 Q1712,592 1752,574 L2224,300 V740 H0 Z"/>
        </clipPath>
      </defs>
      <path class="band-fill" fill="#1450a8" d="M0,300 L40,320 L100,540 L48,540 L60,608 L602,608 L612,560 L1110,418 L1680,580 Q1712,592 1752,574 L2224,300 V740 H0 Z"/>
      <g clip-path="url(#bandClip)">
        <rect role="img" aria-label="Workshop photo of a welder at work with bright sparks flying, tinted blue" x="500" y="380" width="1300" height="360" fill="url(#sparkGlow)"/>
      </g>
      <path class="band-edge" fill="none" stroke="#1ea1dd" stroke-width="7" d="M612,560 L1110,418 L1680,580 Q1712,592 1752,574 L2224,300"/>
      <path class="band-edge" fill="none" stroke="#1ea1dd" stroke-width="7" d="M0,300 L40,320"/>
    </svg>

    <h1 class="brand-name">NORVALE</h1>
    <p class="brand-services">DESIGN/ENGINEERING/FABRICATION</p>

    <div class="divider"></div>

    <h2 class="person-name">ELIAS HARROW</h2>
    <p class="person-role">OPERATIONS<br>MANAGER</p>

    <ul class="contact-list">
      <li class="contact-item contact-phone">
        <svg class="contact-icon" viewBox="0 0 24 24" aria-hidden="true"><path d="M6.6 2.5c.6-.4 1.4-.2 1.8.4l2.1 3.6c.3.6.2 1.3-.3 1.7L8.6 9.6c.9 2.4 2.9 4.8 5.3 6.1l1.5-1.6c.5-.5 1.2-.6 1.8-.2l3.5 2.2c.6.4.8 1.2.4 1.8l-1.3 2.2c-.5.8-1.5 1.2-2.4.9C9.8 18.8 4.6 12.4 3.9 5.9c-.1-.9.4-1.8 1.2-2.3z"/></svg>
        <span class="contact-text">+61 XXX 480 917</span>
      </li>
      <li class="contact-item contact-web">
        <svg class="contact-icon" viewBox="0 0 24 24" aria-hidden="true"><path d="M12 1.5a10.5 10.5 0 1 0 0 21 10.5 10.5 0 0 0 0-21zm7.9 9.5h-3.4a16 16 0 0 0-1.3-6.1A8.5 8.5 0 0 1 19.9 11zM12 3.6c1 1.2 2.3 3.9 2.5 7.4h-5c.2-3.5 1.5-6.2 2.5-7.4zM8.8 4.9A16 16 0 0 0 7.5 11H4.1a8.5 8.5 0 0 1 4.7-6.1zM4.1 13h3.4a16 16 0 0 0 1.3 6.1A8.5 8.5 0 0 1 4.1 13zm7.9 7.4c-1-1.2-2.3-3.9-2.5-7.4h5c-.2 3.5-1.5 6.2-2.5 7.4zm3.2-1.3a16 16 0 0 0 1.3-6.1h3.4a8.5 8.5 0 0 1-4.7 6.1z"/></svg>
        <span class="contact-text">norvale.com.au</span>
      </li>
      <li class="contact-item contact-mail">
        <svg class="contact-icon" viewBox="0 0 24 24" aria-hidden="true"><path d="M1.5 4h21v16h-21zm2.3 2L12 12.6 20.2 6zm-.3 2.5V18h17V8.5L12 15.3z"/></svg>
        <span class="contact-text">staff@norvale.com.au</span>
      </li>
      <li class="contact-item contact-address">
        <svg class="contact-icon" viewBox="0 0 24 24" aria-hidden="true"><path d="M12 1a8 8 0 0 0-8 8c0 5.6 8 14 8 14s8-8.4 8-14a8 8 0 0 0-8-8zm0 11a3 3 0 1 1 0-6 3 3 0 0 1 0 6z"/></svg>
        <span class="contact-text">14-16 Carrick Road<br>Bellmere, WA 6112</span>
      </li>
    </ul>

    <p class="capability-line">PRECISION WELDING FOR COMPLEX SYSTEMS</p>
  </section>
</main>
</body>
</html>
```